Lomtra - 'Destination Metasearch'

We want to make travel research and booking simple and easy within one product by enabling our users to compare destinations.

As such, we are looking for web designers to create mockups of what this ‘destination comparison’ search page could look like. Where possible, we would like for the site to remain using lomtra colours (www.lomtra-example.com).

Attached is a design brief that includes:

1) Company profile
- General information about us
- Audience and markets

2) Project overview
- Problem statement
- What is the project
- Expected deliverables
- Key functionalities
- User flow

An example mockup has been attached.

Designs should be mobile-first

Industry/Entity Type

Travel

Number of Pages Required

1 page

Requirements
Must have
• It must compare a destination using data for both travel and accommodation (see mockup example) and MUST be a mobile design
Nice to have
• Inclusion of additional data points (i.e. weather)
Should not have
• It must not only consider one aspect (i.e. hotel / transport).

```html
<!DOCTYPE html>
<html lang="en">
<head>
<meta charset="utf-8">
<title>Lomtra – Destination Comparison</title>
<link href="https://fonts.googleapis.com/css2?family=Inter:ital,wght@0,400;0,500;0,600;0,700;1,500&display=swap" rel="stylesheet">
<style>
:root{
  --teal:#1a9ba6;
  --ink:#111418;
  --grey:#7b8088;
  --line:#e3e5e8;
  --soft:#eef0f2;
  --bg:#f5f6f7;
  --white:#ffffff;
  --close:#c9ccd1;
}
*{box-sizing:border-box;margin:0;padding:0}
html,body{width:713px;height:1200px;overflow:hidden;background:var(--white)}
body{font-family:"Inter",sans-serif;color:var(--ink)}
.board{position:absolute;left:3px;top:0;width:1484px;height:2520px;transform:scale(0.476);transform-origin:0 0}
.note-top{position:absolute;top:36px;left:0;width:100%;text-align:center;font-size:19px;font-weight:700}
.col-title{position:absolute;font-size:20px;font-weight:700;text-align:center;width:377px}
.phone{position:absolute;width:377px;height:811px;border:3px solid var(--ink);border-radius:22px;overflow:hidden;background:var(--bg);isolation:isolate}
.status{position:absolute;top:0;left:0;right:0;height:50px;background:var(--white);display:flex;justify-content:space-between;align-items:center;padding:0 16px 0 18px;font-size:15px;font-weight:600}
.topbar{position:absolute;top:50px;left:0;right:0;height:58px;background:var(--white);display:flex;align-items:center;padding:0 18px;gap:10px;box-shadow:0 2px 4px rgba(0,0,0,.05)}
.ibtn{width:30px;height:30px;border-radius:4px;background:var(--soft);display:flex;align-items:center;justify-content:center;flex:none}
.ibtn.on{background:var(--teal)}
.search{flex:1;font-size:9px;line-height:13px;color:#555}
.search b{font-weight:600;color:var(--ink)}
.chips{position:absolute;top:124px;left:18px;display:flex;gap:10px}
.chip{height:28px;padding:0 10px;border-radius:3px;background:var(--white);font-size:11.5px;display:flex;align-items:center;min-width:78px;justify-content:center;box-shadow:0 1px 3px rgba(0,0,0,.05)}
.chip.on{background:var(--teal);color:var(--white)}
.stack{position:absolute;top:168px;left:18px;right:18px}
.card{position:relative;background:var(--white);border-radius:6px;padding:14px 16px;box-shadow:0 1px 4px rgba(0,0,0,.05)}
.stack .card{height:180px;margin-bottom:19px}
.x{position:absolute;top:16px;right:14px;width:28px;height:28px;border-radius:50%;background:var(--close);display:flex;align-items:center;justify-content:center}
.name{font-size:13px;font-weight:600;text-transform:uppercase}
.name.teal{color:var(--teal)}
.meta{font-size:13px;color:var(--grey);margin-top:5px}
.meta b{color:var(--ink);font-weight:500}
.meta em{font-style:normal;color:var(--teal);font-weight:600}
.price-row{display:flex;gap:18px;margin-top:12px;font-size:13px;color:var(--grey);align-items:center}
.pi{display:flex;align-items:center;gap:10px}
.ico{width:28px;height:28px;border:1px solid var(--line);border-radius:4px;display:flex;align-items:center;justify-content:center;flex:none}
.ico svg{width:16px;height:16px}
.rule{height:1px;background:var(--line);margin:14px 0}
.actions{display:flex;gap:10px}
.details{flex:1.3;height:40px;border-radius:4px;background:var(--soft);font-size:13px;color:#3d4248;display:flex;align-items:center;justify-content:space-between;padding:0 12px}
.cta{flex:1;height:40px;border-radius:4px;background:var(--teal);color:var(--white);font-size:13px;font-weight:600;display:flex;align-items:center;justify-content:center}
.cta.cancel{background:var(--soft);color:var(--ink);font-weight:500}
/* grid style 1 */
.g1 .card{margin-bottom:22px;height:385px}
.date{font-size:11px;margin-top:6px}
.sec{display:flex;justify-content:space-between;align-items:center;font-size:12.5px;font-weight:600;margin-top:4px}
.mini{height:28px;padding:0 8px;background:var(--soft);border-radius:3px;font-size:11px;font-weight:400;display:flex;align-items:center;gap:8px}
.modes{display:grid;grid-template-columns:118px 112px 1fr;margin-top:14px;font-size:13px}
.mode .lab{display:flex;align-items:center;gap:10px}
.mode .ico{width:26px;height:26px}
.mode p{color:var(--grey);margin-top:8px}
.mode p+p{margin-top:3px}
.total{display:flex;justify-content:space-between;font-size:12.5px;margin-top:6px}
.total small{font-size:8px;color:var(--grey)}
.total .r{text-align:right;color:var(--grey)}
.total .r em{display:block;font-style:normal;color:var(--teal);font-weight:600;margin-top:6px}
.total .l span{display:block;font-size:11px;margin-top:8px}
/* grid style 2 */
.g2{position:absolute;top:168px;left:18px;right:18px;display:grid;grid-template-columns:160px 160px;gap:12px 16px}
.g2 .card{height:280px;padding:14px 12px}
.g2 .meta{margin-top:3px}
.g2 .meta+.meta{margin-top:10px}
.g2 .price-row{margin-top:10px}
.g2 .details{height:40px;flex:none;margin-top:12px;justify-content:center;gap:8px}
.g2 .cta{height:40px;margin-top:10px}
/* coachmark */
.shade{position:absolute;inset:0;background:rgba(20,22,25,.78);z-index:3}
.lift{position:relative;z-index:5}
.tap{position:absolute;top:94px;left:0;right:0;text-align:center;color:var(--white);font-size:13px;font-weight:600;z-index:5}
.tip{position:absolute;top:356px;left:34px;z-index:5;color:var(--white);font-size:13px;font-weight:600;line-height:20px;width:250px}
.tip h4{font-size:22px;font-weight:600;display:flex;align-items:center;gap:4px;margin-bottom:4px}
/* copy */
.copy{position:absolute;font-size:26px;line-height:43px}
.copy ul{list-style:none;padding-left:18px}
.copy li{position:relative;padding-left:25px}
.copy li::before{content:"";position:absolute;left:0;top:17px;width:10px;height:10px;border-radius:50%;background:var(--ink)}
.copy .sub{padding-left:43px}
.statement{position:absolute;top:1310px;left:60px;width:1364px;text-align:center;font-size:27px;line-height:37px;font-weight:500}
.statement i{font-weight:500}
.statement span{color:var(--teal)}
</style>
</head>
<body>
<svg width="0" height="0" style="position:absolute">
  <defs>
    <symbol id="bus" viewBox="0 0 16 16"><rect x="3" y="2" width="10" height="11" rx="2" fill="none" stroke="#111" stroke-width="1.6"/><line x1="3" y1="8" x2="13" y2="8" stroke="#111" stroke-width="1.6"/><circle cx="5.5" cy="10.5" r="1" fill="#111"/><circle cx="10.5" cy="10.5" r="1" fill="#111"/><line x1="5" y1="13" x2="5" y2="15" stroke="#111" stroke-width="1.6"/><line x1="11" y1="13" x2="11" y2="15" stroke="#111" stroke-width="1.6"/></symbol>
    <symbol id="train" viewBox="0 0 16 16"><rect x="4" y="2" width="8" height="10" rx="2" fill="#111"/><rect x="5.5" y="4" width="5" height="3" fill="#fff"/><line x1="5" y1="15" x2="7" y2="12" stroke="#111" stroke-width="1.4"/><line x1="11" y1="15" x2="9" y2="12" stroke="#111" stroke-width="1.4"/></symbol>
    <symbol id="flight" viewBox="0 0 16 16"><path d="M8 1 L9 6 L15 9 L15 10 L9 8.5 L8.8 12.5 L10.5 14 L10.5 15 L8 14 L5.5 15 L5.5 14 L7.2 12.5 L7 8.5 L1 10 L1 9 L7 6 Z" fill="#111"/></symbol>
    <symbol id="hotel" viewBox="0 0 16 16"><rect x="3" y="1.5" width="10" height="13" fill="#111"/><g fill="#fff"><rect x="5" y="3.5" width="2" height="2"/><rect x="9" y="3.5" width="2" height="2"/><rect x="5" y="7" width="2" height="2"/><rect x="9" y="7" width="2" height="2"/><rect x="7" y="11" width="2" height="3.5"/></g></symbol>
    <symbol id="chev" viewBox="0 0 12 12"><path d="M2 4 L6 8 L10 4" fill="none" stroke="#222" stroke-width="1.6"/></symbol>
    <symbol id="x" viewBox="0 0 12 12"><path d="M3 3 L9 9 M9 3 L3 9" stroke="#fff" stroke-width="1.8"/></symbol>
    <symbol id="filter" viewBox="0 0 16 16"><g stroke="#fff" stroke-width="1.5"><line x1="2" y1="4" x2="14" y2="4"/><line x1="2" y1="8" x2="14" y2="8"/><line x1="2" y1="12" x2="14" y2="12"/></g><g fill="#fff"><rect x="9" y="2.5" width="2" height="3"/><rect x="4" y="6.5" width="2" height="3"/><rect x="8" y="10.5" width="2" height="3"/></g></symbol>
    <symbol id="pen" viewBox="0 0 16 16"><path d="M3 13 L4 9.5 L11 2.5 L13.5 5 L6.5 12 Z" fill="#fff"/></symbol>
    <symbol id="grid" viewBox="0 0 16 16"><g fill="currentColor"><rect x="2" y="2" width="5" height="5"/><rect x="9" y="2" width="5" height="5"/><rect x="2" y="9" width="5" height="5"/><rect x="9" y="9" width="5" height="5"/></g></symbol>
    <symbol id="sq" viewBox="0 0 16 16"><rect x="2" y="2" width="12" height="12" rx="2" fill="currentColor"/></symbol>
    <symbol id="list" viewBox="0 0 16 16"><g stroke="currentColor" stroke-width="1.8"><line x1="2" y1="3.5" x2="14" y2="3.5"/><line x1="2" y1="8" x2="14" y2="8"/><line x1="2" y1="12.5" x2="14" y2="12.5"/></g></symbol>
    <symbol id="sig" viewBox="0 0 56 12"><g fill="#111"><rect x="0" y="8" width="3" height="4"/><rect x="4.5" y="6" width="3" height="6"/><rect x="9" y="3.5" width="3" height="8.5"/><rect x="13.5" y="1" width="3" height="11"/></g><path d="M22 5 Q28 0 34 5 M24.5 7.5 Q28 5 31.5 7.5" stroke="#111" stroke-width="1.6" fill="none"/><circle cx="28" cy="10.3" r="1.4" fill="#111"/><rect x="38" y="2" width="17" height="9" rx="2.5" fill="#111"/></symbol>
  </defs>
</svg>

<div class="board">
  <p class="note-top">Please scroll down till the bottom, I explain some interesting information there</p>
  <p class="col-title" style="left:68px;top:86px">UI Mobile View - Grid Style 1</p>
  <p class="col-title" style="left:553px;top:86px">UI Mobile View - List Style 2</p>
  <p class="col-title" style="left:1028px;top:86px">UI Mobile View - Grid Style 2</p>

  <!-- Grid style 1 -->
  <div class="phone" style="left:68px;top:142px">
    <div class="status">19:41<svg width="56" height="12"><use href="#sig"/></svg></div>
    <div class="topbar">
      <span class="ibtn on"><svg width="16" height="16"><use href="#filter"/></svg></span>
      <p class="search">Hamburg, 17-21 Feb | 2 Adults, 1 Child<br><b>Munich, Madrid, Berlin, Jakarta, Ne..</b></p>
      <span class="ibtn on"><svg width="14" height="14"><use href="#pen"/></svg></span>
      <span class="ibtn on" style="color:#fff"><svg width="16" height="16"><use href="#sq"/></svg></span>
      <span class="ibtn" style="color:#777"><svg width="16" height="16"><use href="#list"/></svg></span>
    </div>
    <div class="chips"><span class="chip">Best</span><span class="chip on">Cheapest</span><span class="chip">Shortest Trip</span></div>
    <div class="stack g1">
      <div class="card">
        <span class="x"><svg width="12" height="12"><use href="#x"/></svg></span>
        <p class="name teal">Munich, Germany</p>
        <p class="date">17-21 Feb, 2022 | 4 Days 3 Night</p>
        <div class="rule"></div>
        <div class="sec">TRANSPORTATION<span class="mini">Show Details<svg width="12" height="12"><use href="#chev"/></svg></span></div>
        <div class="modes">
          <div class="mode"><span class="lab"><span class="ico"><svg><use href="#bus"/></svg></span>Bus</span><p>From $40</p><p>12h 15m</p></div>
          <div class="mode"><span class="lab"><span class="ico"><svg><use href="#train"/></svg></span>Train</span><p>From $90</p><p>8h 20m</p></div>
          <div class="mode"><span class="lab"><span class="ico"><svg><use href="#flight"/></svg></span>Flight</span><p>From $160</p><p>1h 45m</p></div>
        </div>
        <div class="rule"></div>
        <div class="sec">ACCOMMODATION<span class="mini">Show Details<svg width="12" height="12"><use href="#chev"/></svg></span></div>
        <div class="modes">
          <div class="mode"><span class="lab"><span class="ico"><svg><use href="#hotel"/></svg></span>Hotel</span><p>From $40</p></div>
          <div class="mode"><span class="lab"><span class="ico"><svg><use href="#hotel"/></svg></span>Apartment</span><p>From $90</p></div>
        </div>
        <div class="rule" style="margin:10px 0 6px"></div>
        <div class="total">
          <div class="l">TOTAL PRICE <small>(incl tax)</small><span>Transportation + Accommodation</span></div>
          <div class="r">start from<em>$552,48</em></div>
        </div>
      </div>
      <div class="card">
        <span class="x"><svg width="12" height="12"><use href="#x"/></svg></span>
        <p class="name teal">Madrid, Spain</p>
        <p class="date">17-21 Feb, 2022 | 4 Days 3 Night</p>
        <div class="rule"></div>
        <div class="sec">TRANSPORTATION<span class="mini">Show Details<svg width="12" height="12"><use href="#chev"/></svg></span></div>
        <div class="modes">
          <div class="mode"><span class="lab"><span class="ico"><svg><use href="#bus"/></svg></span>Bus</span><p>From $80</p><p>26h 30m</p></div>
          <div class="mode"><span class="lab"><span class="ico"><svg><use href="#train"/></svg></span>Train</span><p>From $180</p><p>16h 40m</p></div>
          <div class="mode"><span class="lab"><span class="ico"><svg><use href="#flight"/></svg></span>Flight</span><p>From $320</p><p>3h 30m</p></div>
        </div>
        <div class="rule"></div>
        <div class="sec">ACCOMMODATION<span class="mini">Show Details<svg width="12" height="12"><use href="#chev"/></svg></span></div>
      </div>
    </div>
  </div>

  <!-- List style 2 -->
  <div class="phone" style="left:553px;top:142px">
    <div class="status">19:41<svg width="56" height="12"><use href="#sig"/></svg></div>
    <div class="topbar">
      <span class="ibtn on"><svg width="16" height="16"><use href="#filter"/></svg></span>
      <p class="search">Hamburg, 17-21 Feb | 2 Adults, 1 Child<br><b>Munich, Madrid, Berlin, Jakarta, Ne..</b></p>
      <span class="ibtn on"><svg width="14" height="14"><use href="#pen"/></svg></span>
      <span class="ibtn" style="color:#888"><svg width="16" height="16"><use href="#sq"/></svg></span>
      <span class="ibtn on" style="color:#fff"><svg width="16" height="16"><use href="#list"/></svg></span>
    </div>
    <div class="chips"><span class="chip">Best</span><span class="chip on">Cheapest</span><span class="chip">Shortest Trip</span></div>
    <div class="stack">
      <div class="card"><span class="x"><svg width="12" height="12"><use href="#x"/></svg></span><p class="name">Munich, Germany</p><p class="meta">4 Days 3 Night | <b>from</b> <em>$552,48</em></p><div class="price-row"><span class="pi"><span class="ico"><svg><use href="#bus"/></svg></span>From $40</span><span class="pi"><span class="ico"><svg><use href="#hotel"/></svg></span>From $76</span></div><div class="rule"></div><div class="actions"><span class="details">Show Details<svg width="12" height="12"><use href="#chev"/></svg></span><span class="cta">Compare</span></div></div>
      <div class="card"><span class="x"><svg width="12" height="12"><use href="#x"/></svg></span><p class="name">Madrid, Spain</p><p class="meta">4 Days 3 Night | <b>from</b> <em>$1.000,99</em></p><div class="price-row"><span class="pi"><span class="ico"><svg><use href="#bus"/></svg></span>From $120</span><span class="pi"><span class="ico"><svg><use href="#hotel"/></svg></span>From $90</span></div><div class="rule"></div><div class="actions"><span class="details">Show Details<svg width="12" height="12"><use href="#chev"/></svg></span><span class="cta">Compare</span></div></div>
      <div class="card"><span class="x"><svg width="12" height="12"><use href="#x"/></svg></span><p class="name">Berlin, Germany</p><p class="meta">4 Days 3 Night | <b>from</b> <em>$331,50</em></p><div class="price-row"><span class="pi"><span class="ico"><svg><use href="#bus"/></svg></span>From $90</span><span class="pi"><span class="ico"><svg><use href="#hotel"/></svg></span>From $50</span></div><div class="rule"></div><div class="actions"><span class="details">Show Details<svg width="12" height="12"><use href="#chev"/></svg></span><span class="cta">Compare</span></div></div>
      <div class="card"><span class="x"><svg width="12" height="12"><use href="#x"/></svg></span><p class="name">Jakarta, Indonesia</p><p class="meta">4 Days 3 Night | <b>from</b> <em>$2.007</em></p></div>
    </div>
  </div>

  <!-- Grid style 2 -->
  <div class="phone" style="left:1028px;top:142px">
    <div class="status">19:41<svg width="56" height="12"><use href="#sig"/></svg></div>
    <div class="topbar">
      <span class="ibtn on"><svg width="16" height="16"><use href="#filter"/></svg></span>
      <p class="search">Hamburg, 17-21 Feb | 2 Adults, 1 Child<br><b>Munich, Madrid, Berlin, Jakarta, Ne..</b></p>
      <span class="ibtn on"><svg width="14" height="14"><use href="#pen"/></svg></span>
      <span class="ibtn on" style="color:#fff"><svg width="16" height="16"><use href="#grid"/></svg></span>
      <span class="ibtn" style="color:#777"><svg width="16" height="16"><use href="#list"/></svg></span>
    </div>
    <div class="chips"><span class="chip">Best</span><span class="chip on">Cheapest</span><span class="chip">Shortest Trip</span></div>
    <div class="g2">
      <div class="card"><p class="name">Munich, Germany</p><p class="meta">4 Days 3 Night</p><p class="meta">from <em>$552,48</em></p><div class="price-row"><span class="pi"><span class="ico"><svg><use href="#bus"/></svg></span>From $40</span></div><div class="price-row"><span class="pi"><span class="ico"><svg><use href="#hotel"/></svg></span>From $76</span></div><span class="details">Show Details<svg width="12" height="12"><use href="#chev"/></svg></span><span class="cta">Compare</span></div>
      <div class="card"><p class="name">Madrid, Spain</p><p class="meta">4 Days 3 Night</p><p class="meta">from <em>$552,48</em></p><div class="price-row"><span class="pi"><span class="ico"><svg><use href="#bus"/></svg></span>From $120</span></div><div class="price-row"><span class="pi"><span class="ico"><svg><use href="#hotel"/></svg></span>From $90</span></div><span class="details">Show Details<svg width="12" height="12"><use href="#chev"/></svg></span><span class="cta">Compare</span></div>
      <div class="card"><p class="name">Berlin, Germany</p><p class="meta">4 Days 3 Night</p><p class="meta">from <em>$552,48</em></p><div class="price-row"><span class="pi"><span class="ico"><svg><use href="#bus"/></svg></span>From $40</span></div><div class="price-row"><span class="pi"><span class="ico"><svg><use href="#hotel"/></svg></span>From $76</span></div><span class="details">Show Details<svg width="12" height="12"><use href="#chev"/></svg></span><span class="cta">Compare</span></div>
      <div class="card"><p class="name">Jakarta, Indo...</p><p class="meta">4 Days 3 Night</p><p class="meta">from <em>$552,48</em></p><div class="price-row"><span class="pi"><span class="ico"><svg><use href="#bus"/></svg></span>From $40</span></div><div class="price-row"><span class="pi"><span class="ico"><svg><use href="#hotel"/></svg></span>From $76</span></div><span class="details">Show Details<svg width="12" height="12"><use href="#chev"/></svg></span><span class="cta">Compare</span></div>
    </div>
  </div>

  <div class="copy" style="left:71px;top:980px">
    <p>Revised Style 1 :</p>
    <ul><li>Remove Image</li><li>Move show details dropdown</li><li>Remove CTA</li><li>-Inclusion of other data points</li></ul>
    <p class="sub">a) Duration of trip</p><p class="sub">b) Duration of travel</p>
  </div>
  <div class="copy" style="left:556px;top:980px">
    <p>Revised Style 2 :</p>
    <ul><li>Apply some of the same revisions in Style 1</li><li>Add several compare option</li></ul>
    <p class="sub">a) Direct Filter Button (Best, Cheapest, and Shortest Trip).</p>
    <p class="sub">b) Add Compare Button alonside with ‘Coachmark’</p>
  </div>

  <p class="statement">I agree with '<i>it would be interesting if a user could click a 'compare' button to then have that selected destination's details shown against another card</i>'. And to make it more intuitive when used by User I added a '<span>Coachmark</span>' which works for show a highlight that &nbsp;indicating part of the user interface or to aid the user in learning how to use the system</p>

  <p class="col-title" style="left:68px;top:1506px">First time user</p>
  <p class="col-title" style="left:553px;top:1506px">Click compare button</p>
  <p class="col-title" style="left:1028px;top:1506px">Berlin move under Munich</p>

  <!-- First time user -->
  <div class="phone" style="left:68px;top:1552px">
    <div class="status">19:41<svg width="56" height="12"><use href="#sig"/></svg></div>
    <div class="topbar">
      <span class="ibtn on"><svg width="16" height="16"><use href="#filter"/></svg></span>
      <p class="search">Hamburg, 17-21 Feb | 2 Adults, 1 Child<br><b>Munich, Madrid, Berlin, Jakarta, Ne..</b></p>
      <span class="ibtn on"><svg width="14" height="14"><use href="#pen"/></svg></span>
      <span class="ibtn" style="color:#888"><svg width="16" height="16"><use href="#sq"/></svg></span>
      <span class="ibtn on" style="color:#fff"><svg width="16" height="16"><use href="#list"/></svg></span>
    </div>
    <div class="chips"><span class="chip">Best</span><span class="chip on">Cheapest</span><span class="chip">Shortest Trip</span></div>
    <div class="stack">
      <div class="card"><span class="x"><svg width="12" height="12"><use href="#x"/></svg></span><p class="name">Munich, Germany</p><p class="meta">4 Days 3 Night | <b>from</b> <em>$552,48</em></p><div class="price-row"><span class="pi"><span class="ico"><svg><use href="#bus"/></svg></span>From $40</span><span class="pi"><span class="ico"><svg><use href="#hotel"/></svg></span>From $76</span></div><div class="rule"></div><div class="actions"><span class="details">Show Details<svg width="12" height="12"><use href="#chev"/></svg></span><span class="cta cancel lift" style="background:#fff">Cancel Compare</span></div></div>
      <div class="card"><span class="x"><svg width="12" height="12"><use href="#x"/></svg></span><p class="name">Berlin, Germany</p><p class="meta">4 Days 3 Night | <b>from</b> <em>$331,50</em></p><div class="price-row"><span class="pi"><span class="ico"><svg><use href="#bus"/></svg></span>From $90</span><span class="pi"><span class="ico"><svg><use href="#hotel"/></svg></span>From $50</span></div><div class="rule"></div><div class="actions"><span class="details">Show Details<svg width="12" height="12"><use href="#chev"/></svg></span><span class="cta cancel lift" style="background:#fff">Cancel Compare</span></div></div>
      <div class="card"><span class="x"><svg width="12" height="12"><use href="#x"/></svg></span><p class="name">Madrid, Spain</p><p class="meta">4 Days 3 Night | <b>from</b> <em>$1.000,99</em></p><div class="price-row"><span class="pi"><span class="ico"><svg><use href="#bus"/></svg></span>From $120</span><span class="pi"><span class="ico"><svg><use href="#hotel"/></svg></span>From $90</span></div><div class="rule"></div><div class="actions"><span class="details">Show Details<svg width="12" height="12"><use href="#chev"/></svg></span><span class="cta lift">Compare</span></div></div>
      <div class="card"><span class="x"><svg width="12" height="12"><use href="#x"/></svg></span><p class="name">Jakarta, Indonesia</p><p class="meta">4 Days 3 Night | <b>from</b> <em>$2.007</em></p></div>
    </div>
    <div class="shade"></div>
    <p class="tap">Tap Anywhere to Close</p>
    <div class="tip">
      <h4><svg width="26" height="26" viewBox="0 0 26 26"><g stroke="#fff" stroke-width="1.6"><line x1="13" y1="1" x2="13" y2="4"/><line x1="4" y1="5" x2="6" y2="7"/><line x1="22" y1="5" x2="20" y2="7"/><line x1="1" y1="13" x2="4" y2="13"/><line x1="25" y1="13" x2="22" y2="13"/></g><circle cx="13" cy="13" r="6" fill="#fff"/><rect x="10.5" y="18" width="5" height="4" fill="#fff"/></svg>Pro Tip</h4>
      Click a ‘Compare’ button to compare a destination with another destination easily
    </div>
  </div>

  <!-- Click compare -->
  <div class="phone" style="left:553px;top:1552px">
    <div class="status">19:41<svg width="56" height="12"><use href="#sig"/></svg></div>
    <div class="topbar">
      <span class="ibtn on"><svg width="16" height="16"><use href="#filter"/></svg></span>
      <p class="search">Hamburg, 17-21 Feb | 2 Adults, 1 Child<br><b>Munich, Madrid, Berlin, Jakarta, Ne..</b></p>
      <span class="ibtn on"><svg width="14" height="14"><use href="#pen"/></svg></span>
      <span class="ibtn" style="color:#888"><svg width="16" height="16"><use href="#sq"/></svg></span>
      <span class="ibtn on" style="color:#fff"><svg width="16" height="16"><use href="#list"/></svg></span>
    </div>
    <div class="chips"><span class="chip">Best</span><span class="chip on">Cheapest</span><span class="chip">Shortest Trip</span></div>
    <div class="stack">
      <div class="card"><span class="x"><svg width="12" height="12"><use href="#x"/></svg></span><p class="name">Munich, Germany</p><p class="meta">4 Days 3 Night | <b>from</b> <em>$552,48</em></p><div class="price-row"><span class="pi"><span class="ico"><svg><use href="#bus"/></svg></span>From $40</span><span class="pi"><span class="ico"><svg><use href="#hotel"/></svg></span>From $76</span></div><div class="rule"></div><div class="actions"><span class="details">Show Details<svg width="12" height="12"><use href="#chev"/></svg></span><span class="cta cancel">Cancel Compare</span></div></div>
      <div class="card"><span class="x"><svg width="12" height="12"><use href="#x"/></svg></span><p class="name">Madrid, Spain</p><p class="meta">4 Days 3 Night | <b>from</b> <em>$1.000,99</em></p><div class="price-row"><span class="pi"><span class="ico"><svg><use href="#bus"/></svg></span>From $120</span><span class="pi"><span class="ico"><svg><use href="#hotel"/></svg></span>From $90</span></div><div class="rule"></div><div class="actions"><span class="details">Show Details<svg width="12" height="12"><use href="#chev"/></svg></span><span class="cta">Compare</span></div></div>
      <div class="card"><span class="x"><svg width="12" height="12"><use href="#x"/></svg></span><p class="name">Berlin, Germany</p><p class="meta">4 Days 3 Night | <b>from</b> <em>$331,50</em></p><div class="price-row"><span class="pi"><span class="ico"><svg><use href="#bus"/></svg></span>From $90</span><span class="pi"><span class="ico"><svg><use href="#hotel"/></svg></span>From $50</span></div><div class="rule"></div><div class="actions"><span class="details">Show Details<svg width="12" height="12"><use href="#chev"/></svg></span><span class="cta">Compare</span></div></div>
      <div class="card"><span class="x"><svg width="12" height="12"><use href="#x"/></svg></span><p class="name">Jakarta, Indonesia</p><p class="meta">4 Days 3 Night | <b>from</b> <em>$2.007</em></p></div>
    </div>
  </div>

  <!-- Berlin moved -->
  <div class="phone" style="left:1028px;top:1552px">
    <div class="status">19:41<svg width="56" height="12"><use href="#sig"/></svg></div>
    <div class="topbar">
      <span class="ibtn on"><svg width="16" height="16"><use href="#filter"/></svg></span>
      <p class="search">Hamburg, 17-21 Feb | 2 Adults, 1 Child<br><b>Munich, Madrid, Berlin, Jakarta, Ne..</b></p>
      <span class="ibtn on"><svg width="14" height="14"><use href="#pen"/></svg></span>
      <span class="ibtn" style="color:#888"><svg width="16" height="16"><use href="#sq"/></svg></span>
      <span class="ibtn on" style="color:#fff"><svg width="16" height="16"><use href="#list"/></svg></span>
    </div>
    <div class="chips"><span class="chip">Best</span><span class="chip on">Cheapest</span><span class="chip">Shortest Trip</span></div>
    <div class="stack">
      <div class="card"><span class="x"><svg width="12" height="12"><use href="#x"/></svg></span><p class="name">Munich, Germany</p><p class="meta">4 Days 3 Night | <b>from</b> <em>$552,48</em></p><div class="price-row"><span class="pi"><span class="ico"><svg><use href="#bus"/></svg></span>From $40</span><span class="pi"><span class="ico"><svg><use href="#hotel"/></svg></span>From $76</span></div><div class="rule"></div><div class="actions"><span class="details">Show Details<svg width="12" height="12"><use href="#chev"/></svg></span><span class="cta cancel">Cancel Compare</span></div></div>
      <div class="card"><span class="x"><svg width="12" height="12"><use href="#x"/></svg></span><p class="name">Berlin, Germany</p><p class="meta">4 Days 3 Night | <b>from</b> <em>$331,50</em></p><div class="price-row"><span class="pi"><span class="ico"><svg><use href="#bus"/></svg></span>From $90</span><span class="pi"><span class="ico"><svg><use href="#hotel"/></svg></span>From $50</span></div><div class="rule"></div><div class="actions"><span class="details">Show Details<svg width="12" height="12"><use href="#chev"/></svg></span><span class="cta cancel">Cancel Compare</span></div></div>
      <div class="card"><span class="x"><svg width="12" height="12"><use href="#x"/></svg></span><p class="name">Madrid, Spain</p><p class="meta">4 Days 3 Night | <b>from</b> <em>$1.000,99</em></p><div class="price-row"><span class="pi"><span class="ico"><svg><use href="#bus"/></svg></span>From $120</span><span class="pi"><span class="ico"><svg><use href="#hotel"/></svg></span>From $90</span></div><div class="rule"></div><div class="actions"><span class="details">Show Details<svg width="12" height="12"><use href="#chev"/></svg></span><span class="cta">Compare</span></div></div>
      <div class="card"><span class="x"><svg width="12" height="12"><use href="#x"/></svg></span><p class="name">Jakarta, Indonesia</p><p class="meta">4 Days 3 Night | <b>from</b> <em>$2.007</em></p></div>
    </div>
  </div>
</div>
</body>
</html>
```